Simple Business Cards for Self-employed Coach

Simple business card with a design that includes the QLT logo.
Using either only the logo color or additional colors that match the logo.

Meridian Guides reach deeply into the past, gathering wisdom from East and West, while still staying current with the frontiers of new discovery in cognitive science, genetics, and other disciplines. see https://www.brightharborpath.example/what-is-integral-coaching/

Target Market(s)

Coaching Clients in Tokyo /Asia; in business organizations, but also outside

Industry/Entity Type

Life Coaching

Contact Information for Business Card

Lukas Brenning
Certified Meridian Guide

3-2-48 Kamiyoshi
Nakarino 164-0392
Tokyo, Japan

Phone: +81 70 4817 5062
E-Mail: lukas.brenning@mailora.example

Font styles to use
Sans Serif

Colors
00a990

Requirements
Must have
• include uploaded logo
• color fitting with QLT logo color
Nice to have
• simple, elegant design
Should not have
• clutter

```html
<!DOCTYPE html>
<html lang="en">
<head>
<meta charset="utf-8">
<title>QLT Business Cards</title>
<link rel="stylesheet" href="https://fonts.googleapis.com/css2?family=Jost:wght@300;400;500&display=swap">
<style>
  :root {
    --teal: #017870;
    --paper: #ffffff;
    --backdrop: #e6e7e9;
    --frame: #9a9a9a;
    --ink: #333333;
  }
  * { margin: 0; padding: 0; box-sizing: border-box; }
  html, body { width: 1200px; height: 1002px; overflow: hidden; }
  body {
    background: var(--backdrop);
    font-family: "Jost", sans-serif;
    position: relative;
    border: 1px solid var(--frame);
  }
  .card {
    position: absolute;
    left: 281px;
    width: 638px;
    height: 392px;
    overflow: hidden;
    box-shadow: 0 10px 28px rgba(0,0,0,0.35);
  }
  .card--front { top: 78px; background: var(--teal); color: var(--paper); }
  .card--back { top: 531px; background: var(--paper); color: var(--ink); }
  .card__wedge { position: absolute; left: 0; top: 0; }
  .brand {
    position: absolute;
    left: 72px;
    top: 50px;
    display: flex;
    align-items: center;
    gap: 12px;
    color: var(--teal);
    font-weight: 500;
    font-size: 44px;
    letter-spacing: 6px;
    line-height: 1;
  }
  .brand__mark { width: 34px; height: 34px; background: var(--teal); }
  .contact {
    position: absolute;
    left: 378px;
    top: 0;
    font-weight: 300;
    text-transform: uppercase;
    white-space: nowrap;
  }
  .contact p { position: absolute; left: 0; line-height: 1; font-size: 14.5px; }
  .contact .contact__name { font-size: 20px; top: 167px; }
  .contact__role { top: 191px; }
  .contact__phone { top: 239px; }
  .contact__email { top: 259px; }
  .contact__addr1 { top: 292px; }
  .contact__addr2 { top: 310px; }
  .contact__addr3 { top: 327px; }
</style>
</head>
<body>
  <section class="card card--front">
    <svg class="card__wedge" width="638" height="392" viewBox="0 0 638 392" aria-hidden="true">
      <polygon points="0,0 431,0 150,274 0,122" fill="#ffffff"/>
    </svg>
    <div class="brand"><span class="brand__mark"></span>QLT</div>
    <div class="contact">
      <p class="contact__name">Lukas Brenning</p>
      <p class="contact__role">Certified Meridian Guide</p>
      <p class="contact__phone">+81 70 4817 5062</p>
      <p class="contact__email">lukas.brenning@mailora.example</p>
      <p class="contact__addr1">3-2-48 Kamiyoshi</p>
      <p class="contact__addr2">Nakarino 164-0392</p>
      <p class="contact__addr3">Tokyo, Japan</p>
    </div>
  </section>

  <section class="card card--back">
    <div class="brand"><span class="brand__mark"></span>QLT</div>
    <div class="contact">
      <p class="contact__name">Lukas Brenning</p>
      <p class="contact__role">Certified Meridian Guide</p>
      <p class="contact__phone">+81 70 4817 5062</p>
      <p class="contact__email">lukas.brenning@mailora.example</p>
      <p class="contact__addr1">3-2-48 Kamiyoshi</p>
      <p class="contact__addr2">Nakarino 164-0392</p>
      <p class="contact__addr3">Tokyo, Japan</p>
    </div>
  </section>
</body>
</html>
```